Velvet Heel Ball Poster

We need a poster design for a local event we are holding in our town. The band playing is called "Tinsel" and the theme is "Glam Rock". We would like to see a design that ties in with the Glam Rock theme and it should be very eyecatching. I have attached a file showing the type of look that you might think is suitable but I am open to suggestions! Thanks so much - I am looking forward to seeing your ideas!!

It also needs to say on the poster that the event is sponsored by the Wandoora CRC (see attached logo) and the Wandoora Progress Association (see attached logo)

Industry/Entity Type

Town

Requirements
Must have
• Must have the following wording...

Calling all Rockers...
The Wandoora Progress Association proudly presents live music by
"Tinsel"
Friday 26th October
7:30pm
Wandoora Hall
Tickets $20 - Available from the Wandoora CRC
Dress - GLAM ROCK

```html
<!DOCTYPE html>
<html lang="en">
<head>
<meta charset="utf-8">
<title>Velvet Heel Ball Poster – Tinsel live at Wandoora Hall</title>
<link rel="stylesheet" href="https://fonts.googleapis.com/css2?family=Playfair+Display:wght@400;700;900&family=Bodoni+Moda:opsz,wght@6..96,900&family=Oswald:wght@600&display=swap">
<style>
  :root {
    --stage: #1c1c1f;
    --poster-dark: #0f0f10;
    --poster-mid: #2a2a2b;
    --gold: #f2c84b;
    --magenta: #e21fb6;
    --magenta-deep: #c0179c;
    --white: #ffffff;
    --rule: #6a6a6a;
    --ink: #1a1a1a;
  }
  * { box-sizing: border-box; margin: 0; padding: 0; }
  html, body { width: 1200px; height: 900px; overflow: hidden; }
  body { background: var(--stage); position: relative; font-family: "Playfair Display", Georgia, serif; }

  .poster {
    position: absolute; left: 316px; top: 44px; width: 568px; height: 812px;
    background: radial-gradient(ellipse at 50% 45%, var(--poster-mid) 0%, #1b1b1c 55%, var(--poster-dark) 100%);
    overflow: hidden;
    box-shadow: 0 10px 40px rgba(0,0,0,.6);
  }
  .poster__bands { position: absolute; left: 0; top: 0; width: 568px; height: 330px; }
  .poster__halftone {
    position: absolute; left: 0; top: 0; width: 568px; height: 120px;
    background: linear-gradient(90deg, rgba(242,200,75,.85) 0%, rgba(242,160,60,.55) 35%, rgba(226,31,182,.85) 45%, rgba(226,31,182,.6) 85%, rgba(242,200,75,.5) 100%);
    -webkit-mask: linear-gradient(180deg, #000 0%, rgba(0,0,0,.5) 40%, transparent 100%);
            mask: linear-gradient(180deg, #000 0%, rgba(0,0,0,.5) 40%, transparent 100%);
  }
  .poster__item { position: absolute; left: 57px; white-space: nowrap; }
  .headline { top: 100px; left: 0; width: 568px; text-align: center; font-size: 42px; font-weight: 700; color: var(--gold); letter-spacing: -.5px; }
  .headline__accent { color: var(--magenta); }
  .presenter { top: 159px; left: 0; width: 568px; text-align: center; font-size: 15px; font-weight: 700; color: var(--gold); }
  .intro { top: 200px; left: 0; width: 568px; text-align: center; font-size: 22px; font-weight: 700; color: var(--gold); }
  .band-name {
    top: 240px; left: 0; width: 568px; text-align: center;
    font-family: "Bodoni Moda", "Playfair Display", serif; font-weight: 900; font-size: 88px; letter-spacing: 2px;
    color: var(--white); text-shadow: 6px 6px 10px rgba(0,0,0,.8);
  }
  .rule { position: absolute; left: 57px; width: 454px; border-top: 2px dotted var(--rule); }
  .date { top: 378px; font-size: 31px; font-weight: 700; color: var(--gold); }
  .time { top: 418px; font-size: 31px; font-weight: 700; color: var(--gold); }
  .venue { font-family: "Oswald", "Arial Narrow", sans-serif; font-weight: 600; font-size: 31px; color: var(--magenta); letter-spacing: .5px; margin-left: 8px; }
  .tickets { top: 493px; font-size: 31px; font-weight: 700; color: var(--magenta-deep); }
  .availability { top: 535px; font-size: 23px; font-weight: 700; color: var(--gold); letter-spacing: .3px; }
  .dress { top: 600px; font-size: 30px; font-weight: 700; color: var(--gold); }
  .dress-code { top: 640px; font-size: 26px; font-weight: 700; color: var(--magenta-deep); }
  .band-figures {
    position: absolute; left: 403px; top: 598px; width: 94px; height: 86px;
    background: linear-gradient(180deg, var(--gold), #d9ab2c);
    border-radius: 40px 40px 6px 6px; opacity: .9;
  }

  .sponsors { position: absolute; left: 0; bottom: 0; width: 568px; height: 92px; background: var(--white); }
  .sponsors__label { position: absolute; left: 60px; top: 8px; font-family: Arial, sans-serif; font-size: 9px; font-weight: 700; font-style: italic; color: var(--ink); }
  .sponsor { position: absolute; display: flex; align-items: center; gap: 6px; font-weight: 700; color: var(--ink); }
  .sponsor--council { left: 58px; top: 40px; font-size: 14px; }
  .sponsor--crc { left: 160px; top: 30px; font-size: 11px; line-height: 1.2; }
  .sponsor__mark { width: 14px; height: 14px; background: var(--magenta-deep); }
  .sponsor__mark--round { border-radius: 50%; background: var(--gold); }
</style>
</head>
<body>
  <article class="poster">
    <svg class="poster__bands" viewBox="0 0 568 330" aria-hidden="true">
      <polygon points="0,170 568,60 568,110 0,240" fill="#000" opacity=".35"/>
      <polygon points="0,250 568,110 568,130 0,275" fill="#000" opacity=".45"/>
      <polygon points="0,190 568,70 568,78 0,200" fill="#555" opacity=".35"/>
    </svg>
    <div class="poster__halftone" role="img" aria-label="Gold and magenta halftone dot pattern across the top"></div>

    <h1 class="poster__item headline">Calling all <span class="headline__accent">Rockers...</span></h1>
    <p class="poster__item presenter">The Wandoora Progress Association proudly presents</p>
    <p class="poster__item intro">live music by</p>
    <h2 class="poster__item band-name">TINSEL</h2>

    <div class="rule" style="top:367px"></div>
    <p class="poster__item date">Friday 26th October</p>
    <p class="poster__item time">7:30pm<span class="venue">WANDOORA HALL</span></p>

    <div class="rule" style="top:476px"></div>
    <p class="poster__item tickets">Tickets $20</p>
    <p class="poster__item availability">Available from the Wandoora CRC</p>

    <div class="rule" style="top:585px"></div>
    <p class="poster__item dress">Dress</p>
    <p class="poster__item dress-code">GLAM ROCK</p>
    <div class="band-figures" role="img" aria-label="Gold silhouettes of three glam rock band members"></div>

    <div class="rule" style="top:695px"></div>

    <footer class="sponsors">
      <p class="sponsors__label">Sponsored by</p>
      <div class="sponsor sponsor--council"><span class="sponsor__mark"></span>Wandoora</div>
      <div class="sponsor sponsor--crc"><span class="sponsor__mark sponsor__mark--round"></span><span>Wandoora<br>Community Resource Centre</span></div>
    </footer>
  </article>
</body>
</html>
```